business card for retail pharmacy
Brookfield Pharmacy
Project: business card for retail pharmacy
business card for retail pharmacy - Pharmacy/Pharmaceuticals
Creative Brief
Simple
Gerald P. Ostrander RPh
Owner/Pharmacist
4217 Route 531, Unit #3, Southampton, NJ 08088
brookrxcare7@mailvessel.com
www.brookfieldrxnj-example.com
Hours Monday-Friday 9-7, Saturday 9-1
brookrxcare7 brookrxcare7
Would like to see some cards as red and blue NOT red and gray. We are still not finalized on the logo colors so I would like to see as a red and dark ble combination.
Plidor Plidor

```html
<!DOCTYPE html>
<html lang="en">
<head>
<meta charset="utf-8">
<title>Brookfield Pharmacy – Business Card</title>
<link href="https://fonts.googleapis.com/css2?family=Open+Sans:wght@400;600&display=swap" rel="stylesheet">
<style>
  :root {
    --brand-red: #b3212b;
    --brand-navy: #1b2a4a;
    --paper: #ffffff;
    --backdrop: #e9e9ea;
    --ink-light: #ffffff;
  }
  * { box-sizing: border-box; margin: 0; padding: 0; }
  html, body {
    width: 1200px; height: 901px; overflow: hidden;
    background: var(--backdrop);
    font-family: "Open Sans", Arial, sans-serif;
  }
  .sheet {
    width: 1200px; height: 901px;
    display: flex; flex-direction: column; align-items: center; justify-content: center;
    gap: 53px;
  }
  .card {
    width: 620px; height: 354px; position: relative; overflow: hidden;
    box-shadow: 0 4px 14px rgba(0,0,0,0.18);
  }

  /* Back side */
  .card-back {
    background: var(--brand-navy);
    color: var(--ink-light);
    display: flex; flex-direction: column; align-items: center; justify-content: center;
  }
  .back-mark { display: flex; flex-direction: column; align-items: center; gap: 12px; }
  .back-mark .dot { width: 30px; height: 30px; border-radius: 50%; background: var(--brand-red); }
  .back-mark .name { font-size: 22px; font-weight: 600; letter-spacing: 3px; text-transform: uppercase; }
  .back-rule { width: 210px; height: 1px; background: var(--brand-red); margin: 16px 0 12px; }
  .hours { text-align: center; font-size: 14px; line-height: 1.45; }

  /* Front side */
  .card-front { background: var(--paper); display: flex; }
  .front-brand {
    width: 350px; display: flex; flex-direction: column; align-items: center; justify-content: center; gap: 14px;
  }
  .front-brand .dot { width: 34px; height: 34px; border-radius: 50%; background: var(--brand-red); }
  .front-brand .name {
    color: var(--brand-navy); font-size: 23px; font-weight: 600; letter-spacing: 2px;
    text-transform: uppercase; white-space: nowrap;
  }
  .divider-stripe { width: 5px; background: var(--brand-navy); }
  .divider-gap { width: 7px; }
  .front-details {
    flex: 1; background: var(--brand-red); color: var(--ink-light);
    padding: 56px 12px 0 20px; font-size: 13px; line-height: 1.42;
    border-left: 0;
  }
  .holder { font-size: 15px; font-weight: 600; white-space: nowrap; }
  .role { margin-bottom: 16px; }
  .address { margin-bottom: 12px; }
  .contact-list { list-style: none; }
  .contact-list li { display: flex; align-items: center; gap: 9px; white-space: nowrap; }
  .contact-list svg { width: 12px; height: 12px; flex: none; }
</style>
</head>
<body>
<main class="sheet">
  <section class="card card-back" aria-label="Card back">
    <div class="back-mark">
      <span class="dot"></span>
      <span class="name">Brookfield Pharmacy</span>
    </div>
    <div class="back-rule"></div>
    <p class="hours">Hours:<br>Monday-Friday 9-7, Saturday 9-1</p>
  </section>

  <section class="card card-front" aria-label="Card front">
    <div class="front-brand">
      <span class="dot"></span>
      <span class="name">Brookfield Pharmacy</span>
    </div>
    <div class="divider-stripe"></div>
    <div class="divider-gap"></div>
    <div class="front-details">
      <p class="holder">Gerald P. Ostrander RPh</p>
      <p class="role">Owner/Pharmacist</p>
      <p class="address">4217 Route 531, Unit #3<br>Southampton, NJ 08088</p>
      <ul class="contact-list">
        <li>
          <svg viewBox="0 0 12 12" aria-hidden="true"><path fill="#fff" d="M2.5 1h2l1 2.5-1.3 1a6 6 0 0 0 3.3 3.3l1-1.3L11 7.5v2A1.5 1.5 0 0 1 9.5 11 8.5 8.5 0 0 1 1 2.5 1.5 1.5 0 0 1 2.5 1z"/></svg>
          609-555-0142
        </li>
        <li>
          <svg viewBox="0 0 12 12" aria-hidden="true"><rect x="1" y="1" width="10" height="10" rx="1.5" fill="#fff"/><rect x="3" y="3" width="6" height="3" fill="#b3212b"/></svg>
          609-555-0147
        </li>
        <li>
          <svg viewBox="0 0 12 12" aria-hidden="true"><rect x="0.5" y="2.5" width="11" height="7" rx="1" fill="#fff"/><path d="M1 3l5 3.5L11 3" stroke="#b3212b" fill="none"/></svg>
          brookrxcare7@mailvessel.com
        </li>
        <li>
          <svg viewBox="0 0 12 12" aria-hidden="true"><circle cx="6" cy="6" r="5" fill="none" stroke="#fff" stroke-width="1.3"/><path d="M1 6h10M6 1c-2.5 3-2.5 7 0 10M6 1c2.5 3 2.5 7 0 10" stroke="#fff" fill="none"/></svg>
          www.brookfieldrxnj-example.com
        </li>
      </ul>
    </div>
  </section>
</main>
</body>
</html>
```